Bramblecourt Homes Stationary
Fast Settlements
Professional
Dorian Pelletier
Managing Member
4817 Larkspur Ave Suite 210
Washington, DC
dgpelletier@bramblecourthomes.net
www.bramblecourthomes.net
Business License # 782645113058
Cash Buyer, Fast Closing.
Residential and Commercial
We are a Nation Wide Buyer.
will upload ai file shortly
vector logo file

```html
<!DOCTYPE html>
<html lang="en">
<head>
<meta charset="utf-8">
<title>Bramblecourt Homes Stationary</title>
<link href="https://fonts.googleapis.com/css2?family=Montserrat:wght@400;600;800&display=swap" rel="stylesheet">
<style>
  :root {
    --green: #1f8f3f;
    --green-dark: #14672c;
    --ink: #3a3a3a;
    --grey: #6d6d6d;
    --paper: #ffffff;
    --backdrop: #e9ebea;
  }
  * { margin: 0; padding: 0; box-sizing: border-box; }
  html, body { width: 1200px; height: 1006px; overflow: hidden; }
  body {
    background: var(--backdrop);
    font-family: "Montserrat", Arial, sans-serif;
    position: relative;
  }
  .card {
    position: absolute;
    left: 220px;
    width: 760px;
    height: 434px;
    background: var(--paper);
    border-radius: 18px;
    overflow: hidden;
    box-shadow: 0 6px 24px rgba(0,0,0,0.12);
  }
  .card--front { top: 42px; }
  .card--back { top: 530px; }

  .brand-name {
    color: var(--green);
    font-weight: 800;
    text-transform: uppercase;
    letter-spacing: 2px;
    display: flex;
    align-items: center;
    gap: 14px;
    white-space: nowrap;
  }
  .brand-name .mark {
    width: 22px; height: 22px; background: var(--green); flex: none;
  }

  .front-brand {
    position: absolute; top: 150px; left: 0; right: 0;
    justify-content: center; font-size: 44px;
  }
  .front-rule {
    position: absolute; top: 232px; left: 170px; right: 170px;
    height: 2px; background: var(--ink);
  }
  .front-web {
    position: absolute; top: 248px; left: 0; right: 0; text-align: center;
    font-size: 17px; letter-spacing: 4px; color: var(--ink); font-weight: 600;
  }

  .back-brand { position: absolute; top: 44px; left: 44px; font-size: 30px; }
  .contact-list {
    position: absolute; top: 112px; left: 44px; list-style: none;
    font-size: 14px; color: var(--ink); letter-spacing: 1px;
  }
  .contact-list li { display: flex; align-items: center; gap: 10px; height: 23px; white-space: nowrap; }
  .contact-list svg { width: 16px; height: 16px; flex: none; }

  .person {
    position: absolute; right: 46px; top: 300px; text-align: left;
    font-size: 15px; letter-spacing: 1.5px;
  }
  .person-name { color: var(--green); font-weight: 600; }
  .person-title { color: var(--grey); font-weight: 400; margin-top: 4px; }

  .footer-band { position: absolute; left: 0; bottom: 0; width: 760px; height: 120px; }
  .footer-web {
    position: absolute; right: 46px; bottom: 26px; color: var(--paper);
    font-size: 15px; letter-spacing: 3px; font-weight: 600;
  }
</style>
</head>
<body>

<section class="card card--front">
  <div class="brand-name front-brand"><span class="mark"></span>Bramblecourt Homes</div>
  <div class="front-rule"></div>
  <div class="front-web">www.BramblecourtHomes.net</div>
</section>

<section class="card card--back">
  <div class="brand-name back-brand"><span class="mark"></span>Bramblecourt Homes</div>

  <ul class="contact-list">
    <li>
      <svg viewBox="0 0 16 16"><circle cx="8" cy="8" r="8" fill="var(--green)"/><path d="M8 3.5a3 3 0 0 0-3 3c0 2.2 3 6 3 6s3-3.8 3-6a3 3 0 0 0-3-3zm0 4a1 1 0 1 1 0-2 1 1 0 0 1 0 2z" fill="#fff"/></svg>
      4817 Larkspur Ave Suite 210
    </li>
    <li>
      <svg viewBox="0 0 16 16"><circle cx="8" cy="8" r="8" fill="var(--green)"/></svg>
      Alderbrook, VA 22150
    </li>
    <li>
      <svg viewBox="0 0 16 16"><circle cx="8" cy="8" r="8" fill="var(--green)"/><path d="M5 4h2l1 2.5-1.2.8a6 6 0 0 0 2.9 2.9l.8-1.2L13 10v2a1 1 0 0 1-1 1A8 8 0 0 1 4 5a1 1 0 0 1 1-1z" fill="#fff"/></svg>
      202-555-0147
    </li>
    <li>
      <svg viewBox="0 0 16 16"><circle cx="8" cy="8" r="8" fill="var(--green)"/><path d="M5 4h2l1 2.5-1.2.8a6 6 0 0 0 2.9 2.9l.8-1.2L13 10v2a1 1 0 0 1-1 1A8 8 0 0 1 4 5a1 1 0 0 1 1-1z" fill="#fff"/></svg>
      410-555-0192
    </li>
    <li>
      <svg viewBox="0 0 16 16"><circle cx="8" cy="8" r="8" fill="var(--green)"/><path d="M4 5h8v6H4z" fill="none" stroke="#fff"/><path d="M4 5l4 3.5L12 5" fill="none" stroke="#fff"/></svg>
      dgpelletier@bramblecourthomes.net
    </li>
    <li>
      <svg viewBox="0 0 16 16"><circle cx="8" cy="8" r="8" fill="var(--green)"/><circle cx="8" cy="8" r="4" fill="none" stroke="#fff"/><path d="M4 8h8M8 4v8" stroke="#fff" stroke-width="0.8"/></svg>
      www.bramblecourthomes.net
    </li>
  </ul>

  <div class="person">
    <div class="person-name">Dorian Pelletier</div>
    <div class="person-title">Managing Member</div>
  </div>

  <svg class="footer-band" viewBox="0 0 760 120" preserveAspectRatio="none">
    <path d="M0 40 H300 C340 40 350 70 390 70 H760 V120 H0 Z" fill="var(--green)"/>
    <path d="M0 28 H300 C340 28 350 58 390 58 H760 V70 H390 C350 70 340 40 300 40 H0 Z" fill="#4a4a4a"/>
    <path d="M0 40 H300 C340 40 350 70 390 70 H400 C360 70 345 52 300 52 H0 Z" fill="var(--green-dark)"/>
  </svg>
  <div class="footer-web">www.BramblecourtHomes.net</div>
</section>

</body>
</html>
```